The Marisol & Jocelyn Fruit Co.

We produce a very high quality freeze dried fruit, all organic, no preservative, no additives, nothing but the fruit. To get more use out of a facility we have in Charlotte, we decided to pursue some high end online retailers with a high end freeze dried organic fruit. We are looking for a very high end, upper east side, trendy, hip, logo and package design for this. There are 4 SKU's - Freeze Dried Strawberries, Freeze Dried Blueberries, Freeze Dried Cherries, and a blend of of all 3 as the 4th SKU. 2 labels each that are 6" x 6" - The front, again needs to be fun and trendy big bold etc. Nothing frilly and Quiet Barn by the creek. The back needs to contain the nutritional statements for each and some copy describing the product and the company.
Updates
This would be one of only a few competitors in this segment
We are looking to steal a page from the wine industry. The coolest looking label on the shelf wins over the uneducated wine buyer. The designs are all fine, but they need to be sleeker, sexier, funner, etc. Someone should look at the label and say....wow that is FUN AND SEXY! I have to buy some! VORBEX.COM screams that. Don't worry so much about pictures of the fruit as the bag is going to be clear. Sell the brand not the fruit. OK?
Reason: Why not?
Reason: Final Selection by Monday 5pm EST.
For all designs that have not been eliminated:
Reason: Final selections. All four designs front and back on one file uploaded by noon tomorrow ( 12:01 PM EST New York)
Target Market(s)
People that would shop at sites like www.vorbex.com
Industry/Entity Type
It Company
Requirements
Nice to have
- The brand is named after our two daughters - One is very girly and the other is very "sassy" It would be fun to have the logo capture their personalities a little. I have uploaded a picture. Marisol on the left, Jocelyn on the right.
Also, another of our brands, Hank Pellow, packaging is attached here. Some consistency in look and feel may be good.
Should not have
- Nothing frilly or dainty, or delicate. Colorful fun and bold but trendy.

```html
<!DOCTYPE html>
<html lang="en">
<head>
<meta charset="utf-8">
<title>The Marisol &amp; Jocelyn Fruit Co. — Freeze Dried Labels</title>
<link rel="stylesheet" href="https://fonts.googleapis.com/css2?family=Open+Sans:wght@600;700&family=Yellowtail&display=swap">
<style>
  :root {
    --backdrop: #1d1c1b;
    --backdrop-edge: #3a3938;
    --pink-band: #e0158a;
    --pink-panel: #e6217f;
    --pink-glow: #f7c4dc;
    --red-band: #e71a1f;
    --red-panel: #e8191f;
    --red-glow: #f8c3c3;
    --white: #ffffff;
    --ink: #111111;
    --logo-ink: #333333;
  }
  html, body {
    margin: 0;
    padding: 0;
    width: 1200px;
    height: 1000px;
    overflow: hidden;
    background: var(--backdrop);
  }
  .canvas {
    position: relative;
    width: 1200px;
    height: 1000px;
    background: var(--backdrop);
    box-sizing: border-box;
    border: 1px solid var(--backdrop-edge);
  }
  .label {
    position: absolute;
    top: 237px;
    width: 484px;
    height: 504px;
  }
  .label--strawberries { left: 97px; }
  .label--cherries { left: 600px; }
  .label svg { display: block; overflow: visible; }
  .brand-name {
    font-family: "Open Sans", sans-serif;
    font-weight: 600;
    font-size: 9.5px;
    fill: var(--logo-ink);
  }
  .kicker {
    font-family: "Open Sans", sans-serif;
    font-weight: 700;
    font-size: 16px;
    fill: var(--white);
  }
  .product-name {
    font-family: "Yellowtail", cursive;
    font-size: 72px;
    fill: var(--white);
    stroke: var(--ink);
    stroke-width: 6px;
    paint-order: stroke fill;
    stroke-linejoin: round;
  }
  .product-shadow {
    font-family: "Yellowtail", cursive;
    font-size: 72px;
    fill: var(--ink);
    stroke: var(--ink);
    stroke-width: 6px;
    stroke-linejoin: round;
  }
</style>
</head>
<body>
<main class="canvas">

  <section class="label label--strawberries" aria-label="Freeze Dried Strawberries label">
    <svg width="484" height="504" viewBox="0 0 484 504">
      <defs>
        <radialGradient id="pink-burst" cx="242" cy="400" r="330" gradientUnits="userSpaceOnUse">
          <stop offset="0" stop-color="var(--white)"/>
          <stop offset="0.3" stop-color="var(--pink-glow)"/>
          <stop offset="0.75" stop-color="var(--pink-panel)"/>
        </radialGradient>
        <linearGradient id="strawberry-tone" x1="0" y1="0" x2="1" y2="1">
          <stop offset="0" stop-color="#6fbf3a"/>
          <stop offset="0.5" stop-color="#e8493f"/>
          <stop offset="1" stop-color="#c21f28"/>
        </linearGradient>
        <clipPath id="pink-inner">
          <path d="M16,150 C16,52 72,20 242,20 C412,20 468,52 468,150 L468,330 C468,440 372,488 242,488 C112,488 16,440 16,330 Z"/>
        </clipPath>
      </defs>
      <path class="label-band" fill="var(--pink-band)" d="M0,150 C0,38 62,4 242,4 C422,4 484,38 484,150 L484,330 C484,452 380,504 242,504 C104,504 0,452 0,330 Z"/>
      <g clip-path="url(#pink-inner)">
        <rect x="0" y="0" width="484" height="504" fill="url(#pink-burst)"/>
        <path class="brand-cap" fill="var(--white)" d="M0,0 H484 V58 C450,56 420,32 380,30 C340,28 320,66 242,68 C164,66 144,28 104,30 C64,32 34,56 0,58 Z"/>
      </g>
      <path class="label-rule" fill="none" stroke="var(--white)" stroke-width="3" d="M16,150 C16,52 72,20 242,20 C412,20 468,52 468,150 L468,330 C468,440 372,488 242,488 C112,488 16,440 16,330 Z"/>
      <text class="brand-name" x="242" y="43" text-anchor="middle">The Marisol &amp; Jocelyn Fruit Co.</text>
      <g transform="rotate(-6 242 180)">
        <text class="kicker" x="150" y="146">Freeze Dried</text>
        <text class="product-shadow" x="246" y="222" text-anchor="middle" textLength="380" lengthAdjust="spacingAndGlyphs">Strawberries</text>
        <text class="product-name" x="242" y="216" text-anchor="middle" textLength="380" lengthAdjust="spacingAndGlyphs">Strawberries</text>
      </g>
      <g role="img" aria-label="Illustration of two ripe strawberries with green leaves">
        <rect x="126" y="280" width="212" height="156" rx="70" fill="url(#strawberry-tone)"/>
      </g>
    </svg>
  </section>

  <section class="label label--cherries" aria-label="Freeze Dried Cherries label">
    <svg width="484" height="504" viewBox="0 0 484 504">
      <defs>
        <radialGradient id="red-burst" cx="242" cy="400" r="330" gradientUnits="userSpaceOnUse">
          <stop offset="0" stop-color="var(--white)"/>
          <stop offset="0.3" stop-color="var(--red-glow)"/>
          <stop offset="0.75" stop-color="var(--red-panel)"/>
        </radialGradient>
        <linearGradient id="cherry-tone" x1="0" y1="0" x2="0" y2="1">
          <stop offset="0" stop-color="#8fb04a"/>
          <stop offset="0.45" stop-color="#b3202c"/>
          <stop offset="1" stop-color="#7a0d16"/>
        </linearGradient>
        <clipPath id="red-inner">
          <path d="M16,150 C16,52 72,20 242,20 C412,20 468,52 468,150 L468,330 C468,440 372,488 242,488 C112,488 16,440 16,330 Z"/>
        </clipPath>
      </defs>
      <path class="label-band" fill="var(--red-band)" d="M0,150 C0,38 62,4 242,4 C422,4 484,38 484,150 L484,330 C484,452 380,504 242,504 C104,504 0,452 0,330 Z"/>
      <g clip-path="url(#red-inner)">
        <rect x="0" y="0" width="484" height="504" fill="url(#red-burst)"/>
        <path class="brand-cap" fill="var(--white)" d="M0,0 H484 V58 C450,56 420,32 380,30 C340,28 320,66 242,68 C164,66 144,28 104,30 C64,32 34,56 0,58 Z"/>
      </g>
      <path class="label-rule" fill="none" stroke="var(--white)" stroke-width="3" d="M16,150 C16,52 72,20 242,20 C412,20 468,52 468,150 L468,330 C468,440 372,488 242,488 C112,488 16,440 16,330 Z"/>
      <text class="brand-name" x="242" y="43" text-anchor="middle">The Marisol &amp; Jocelyn Fruit Co.</text>
      <g transform="rotate(-6 242 180)">
        <text class="kicker" x="200" y="144">Freeze Dried</text>
        <text class="product-shadow" x="246" y="220" text-anchor="middle" textLength="320" lengthAdjust="spacingAndGlyphs">Cherries</text>
        <text class="product-name" x="242" y="214" text-anchor="middle" textLength="320" lengthAdjust="spacingAndGlyphs">Cherries</text>
      </g>
      <g role="img" aria-label="Illustration of a bunch of red cherries on stems with leaves">
        <rect x="142" y="248" width="224" height="204" rx="60" fill="url(#cherry-tone)"/>
      </g>
    </svg>
  </section>

</main>
</body>
</html>
```